Business Card Design for Occupational Medicine Start Up Company

We need to design a professional business card. We are a healthcare company providing occupational medicine services to blue collar industries. We are professional, efficient and high quality service providers.

Target Market(s)

Blue Collar Industry: Shipbuilding, Ports, Trucking Companies; The Executives and Safety Officers for these companies

Industry/Entity Type

Healthcare

Contact Information for Business Card

Logo, Name, Title, Email, Phone

Other font styles liked:
• Please match our Brand Guide

Requirements
Must have
• Our Company Colors and Logo

```html
<!DOCTYPE html>
<html lang="en">
<head>
<meta charset="utf-8">
<title>FieldCare Clinics — Business Card</title>
<link href="https://fonts.googleapis.com/css2?family=Montserrat:wght@400;500;700&display=swap" rel="stylesheet">
<style>
  :root {
    --backdrop: #e3e3e3;
    --card-white: #ffffff;
    --navy: #2b3580;
    --sky: #27a9e1;
    --amber: #f5b14c;
    --grey-text: #6f6f6f;
    --white: #ffffff;
  }
  * { margin: 0; padding: 0; box-sizing: border-box; }
  html, body {
    width: 1200px;
    height: 900px;
    overflow: hidden;
    background: var(--backdrop);
    font-family: "Montserrat", sans-serif;
  }
  .canvas {
    position: relative;
    width: 1200px;
    height: 900px;
  }
  .card {
    position: absolute;
    left: 320px;
    width: 560px;
    height: 320px;
  }
  .card--front { top: 110px; background: var(--card-white); }
  .card--back  { top: 470px; background: var(--navy); }

  /* front face */
  .brand-block {
    position: absolute;
    left: 40px;
    top: 84px;
    width: 152px;
    text-align: center;
  }
  .brand-block__dot {
    display: block;
    width: 72px;
    height: 72px;
    margin: 0 auto 12px;
    border-radius: 50%;
    background: var(--navy);
  }
  .brand-block__name {
    color: var(--navy);
    font-weight: 700;
    font-size: 15px;
    letter-spacing: 0.04em;
    line-height: 1.25;
    text-transform: uppercase;
  }
  .divider {
    position: absolute;
    left: 215px;
    top: 64px;
    width: 2px;
    height: 193px;
    background: var(--amber);
  }
  .contact {
    position: absolute;
    left: 241px;
    top: 104px;
  }
  .contact__name {
    color: var(--navy);
    font-size: 20px;
    font-weight: 400;
    letter-spacing: 0.02em;
    line-height: 1.2;
  }
  .contact__name strong { font-weight: 700; }
  .contact__title {
    color: var(--grey-text);
    font-size: 17.5px;
    font-weight: 400;
    letter-spacing: 0.02em;
    margin-top: 2px;
  }
  .contact__line {
    color: var(--grey-text);
    font-size: 15.5px;
    font-weight: 400;
    letter-spacing: 0.02em;
  }
  .contact__line--email { margin-top: 30px; }
  .contact__line--phone { margin-top: 10px; }

  /* back face */
  .lockup {
    position: absolute;
    left: 62px;
    top: 112px;
    display: flex;
    align-items: center;
    gap: 34px;
  }
  .lockup__dot {
    width: 96px;
    height: 96px;
    border-radius: 50%;
    background: var(--sky);
  }
  .lockup__name {
    color: var(--white);
    font-weight: 500;
    font-size: 33px;
    letter-spacing: 0.04em;
    line-height: 1.1;
    text-transform: uppercase;
  }
</style>
</head>
<body>
<main class="canvas">
  <section class="card card--front" aria-label="Business card front">
    <div class="brand-block">
      <span class="brand-block__dot"></span>
      <p class="brand-block__name">FieldCare<br>Clinics</p>
    </div>
    <div class="divider"></div>
    <div class="contact">
      <p class="contact__name"><strong>DANIEL</strong> MARSH</p>
      <p class="contact__title">Cardiac Sonographer</p>
      <p class="contact__line contact__line--email">daniel.marsh@fieldcareclinics.com</p>
      <p class="contact__line contact__line--phone">555-018-2740</p>
    </div>
  </section>

  <section class="card card--back" aria-label="Business card back">
    <div class="lockup">
      <span class="lockup__dot"></span>
      <p class="lockup__name">FieldCare Clinics</p>
    </div>
  </section>
</main>
</body>
</html>
```